Dutch craft distillery needs labels designed for Gin bottle

We are a small craft distillery based in The Netherlands. We are currently producing only GIN. While we do have a logo for our distillery, we are still in search of a winning design for our Gin bottle. We are looking for something modern yet classy. Let your creativity run wild. Play around with colours, think out of the box….The winning designer will be challenged to create the coolest labels for the different flavours of Gin we will be producing in the near future. The label will maintain the same design elements throughout the design, but will also be able to differentiate each variety clearly. So for e.g. A flowery Vantoor Gin can have a pink label with a different description and a spicy Vantoor gin can have another colour with another description and so on. If the design really appeals to us, we might also invite the designer to do our website for us!

In a nutshell: It is a 500 ml bottle, (Please check the attachment so you get an idea as to what kind of bottle to imagine while making the labels). The bottle is going to have a light coloured wooden lid/cork to it. As of now we have a transparent seal to complete the sealing process once the bottling is done. The idea is that we will have two labels. One in the front and one behind. The size of the labels are as follows:

Front label: 102 x 76 mm the front label. (TO BE USED HORIZONTALLY). The details that we need on the front label are in a separate attachment.

Back label: The size for the label at the back of the bottle is: 76 x 51 mm (TO BE USED VERTICALLY) The information that needs to come on the label behind is also in the same document which is attached separately. The label behind will also have batch no. & date (Please refer to attachment to understand what I mean by batch no. date, distiller’s signature etc.) I have attached a picture of an already existing brand which has its batch number and distillers signature etc on it….so you can understand what I exactly mean by that. Please do not copy their design, this is purely to give you an idea as to what I mean by batch number and so on. The address of the distillery can be put horizontally, vertically, on the side along one border, or however you find appropriate. This is the address:
Klaverhoekstraat 41,
6318 KT, Hengelo.
The Netherlands.
www.vantoor.nl

Logo’s no drinking when pregnant, No driving and drinking, No drinking under the age of 18 need to be present on the label behind. Alternately, we can also have www.calm-sipping.com instead of the under 18 no alcohol sign, most alcohol bottles these days have it. Please let me know what else you would need from me for this. So be creative and do your best!

Thanks and regards, Marisol Vendekampa.

Target Market(s)

Largely males and females between 25-55 , the audience could even be slightly older.

Colors

Designer to choose colors to be used in the design.

Requirements
Must have
• 1) The labels need to be modern, yet classy, elite..
• 2) We need to specify the fact that we are a craft distillery and the gin is HANDMADE, using only the highest quality ingredients.
• 3) We at Vantoor live, breathe, dream, talk about our dream which is our distillery and its product. The label needs to bring home this point and should clearly specify and mention that it is produced and bottled in The Netherlands. Or handmade and bottled with love and passion in The Netherlands or something to that effect if it matches with the rest of the design.
• 4) The colours you chose must match in some way or the other with the colours used for the logo design.
Nice to have
• Would be nice to have colours and look bold, although not completely necessary.
Should not have
• What I definitely do not want is something too whacky like a skull or some kind of vague work of art. For the rest, I leave it upto you….!

```html
<!DOCTYPE html>
<html lang="en">
<head>
<meta charset="utf-8">
<title>Vantoor Gin – Label Options</title>
<link href="https://fonts.googleapis.com/css2?family=Rye&family=Montserrat:wght@500;600;700&family=Roboto+Slab:wght@400;600&family=Playfair+Display:wght@700&family=Oswald:wght@300&family=Tinos&display=swap" rel="stylesheet">
<style>
  :root {
    --navy: #231c36;
    --orange: #ef7f3f;
    --brand-red: #e9573a;
    --paper: #ebebea;
    --bar-grey: #55575c;
    --backdrop-light: #7a7a7a;
    --backdrop-dark: #333333;
    --white: #ffffff;
  }
  html, body {
    margin: 0;
    padding: 0;
    overflow: hidden;
  }
  .board {
    position: relative;
    width: 1200px;
    height: 900px;
    overflow: hidden;
    background: radial-gradient(ellipse at 50% 45%, var(--backdrop-light) 0%, var(--backdrop-dark) 100%);
  }
  .label {
    position: absolute;
    display: block;
  }
  .label--classic-dark { left: 28px; top: 38px; }
  .label--classic-orange { left: 617px; top: 38px; }
  .label--badge { left: 300px; top: 472px; }

  .option-caption {
    position: absolute;
    margin: 0;
    font-family: "Oswald", sans-serif;
    font-weight: 300;
    font-size: 31px;
    letter-spacing: 4px;
    color: var(--white);
  }
  .option-caption--1 { left: 146px; top: 500px; }
  .option-caption--2 { left: 932px; top: 486px; }
  .option-caption--3 { left: 134px; top: 816px; }

  .tag { font-family: "Tinos", serif; font-size: 10px; fill: var(--navy); }
  .brand { font-family: "Montserrat", sans-serif; font-weight: 700; fill: var(--brand-red); }
  .title { font-family: "Rye", serif; }
  .caps-serif { font-family: "Roboto Slab", serif; font-weight: 600; fill: var(--navy); }
  .caps-sans { font-family: "Montserrat", sans-serif; font-weight: 600; }
  .spec { font-family: "Tinos", serif; fill: var(--navy); }
</style>
</head>
<body>
<main class="board">

  <svg width="0" height="0" style="position:absolute" aria-hidden="true">
    <defs>
      <symbol id="corner-bracket" viewBox="0 0 130 100" overflow="visible">
        <path d="M4 100 V4 H110" fill="none" stroke="var(--navy)" stroke-width="5"/>
        <path d="M14 92 V14 H100" fill="none" stroke="var(--navy)" stroke-width="1.5"/>
        <path d="M24 80 A56 56 0 0 1 80 24" fill="none" stroke="var(--navy)" stroke-width="2"/>
      </symbol>
    </defs>
  </svg>

  <!-- Option 1 -->
  <svg class="label label--classic-dark" width="570" height="430" viewBox="0 0 570 430">
    <rect width="570" height="430" fill="var(--paper)"/>
    <g class="frame">
      <use href="#corner-bracket" x="26" y="26" width="130" height="100"/>
      <use href="#corner-bracket" width="130" height="100" transform="translate(544 26) scale(-1 1)"/>
      <use href="#corner-bracket" width="130" height="100" transform="translate(26 404) scale(1 -1)"/>
      <use href="#corner-bracket" width="130" height="100" transform="translate(544 404) scale(-1 -1)"/>
    </g>
    <text class="tag" x="137" y="82" text-anchor="middle">100% Natural Botanicals</text>
    <line x1="85" y1="89" x2="189" y2="89" stroke="var(--navy)" stroke-width="1"/>
    <text class="tag" x="435" y="82" text-anchor="middle">No Artificial Flavouring</text>
    <line x1="383" y1="89" x2="487" y2="89" stroke="var(--navy)" stroke-width="1"/>

    <text class="brand" text-anchor="middle"><tspan x="285" y="84" font-size="28" letter-spacing="2">VANTOOR</tspan><tspan x="285" y="114" font-size="13" letter-spacing="4">DISTILLERY</tspan></text>

    <text class="title" x="285" y="194" text-anchor="middle" font-size="66" fill="var(--navy)" textLength="380" lengthAdjust="spacingAndGlyphs">VANTOOR</text>
    <polygon points="158,228 240,226 240,236 168,236" fill="var(--bar-grey)"/>
    <polygon points="330,226 412,228 402,236 330,236" fill="var(--bar-grey)"/>
    <text class="title" x="285" y="242" text-anchor="middle" font-size="52" fill="var(--navy)" textLength="104" lengthAdjust="spacingAndGlyphs">GIN</text>
    <line x1="190" y1="256" x2="380" y2="256" stroke="var(--navy)" stroke-width="1"/>
    <text class="caps-serif" x="285" y="269" text-anchor="middle" font-size="11" letter-spacing="1.5">PREMIUM</text>
    <text class="caps-serif" x="285" y="287" text-anchor="middle" font-size="11" textLength="360" lengthAdjust="spacing">DISTILLED AND BOTTLED BY VANTOOR DISTILLERY</text>
    <text class="caps-sans" x="285" y="318" text-anchor="middle" font-size="27" fill="var(--orange)" textLength="288" lengthAdjust="spacingAndGlyphs">LONDON DRY GIN</text>
    <text class="caps-serif" x="285" y="331" text-anchor="middle" font-size="8" letter-spacing="0.5">HANDCRAFTED IN SMALL BATCH</text>
    <line x1="165" y1="336" x2="405" y2="336" stroke="var(--navy)" stroke-width="1"/>
    <line x1="176" y1="348" x2="410" y2="348" stroke="var(--navy)" stroke-width="1"/>
    <line x1="176" y1="373" x2="410" y2="373" stroke="var(--navy)" stroke-width="1"/>
    <text class="spec" x="214" y="365" text-anchor="middle" font-size="10">50 CL|43% ALC.</text>
    <ellipse cx="283" cy="361" rx="31" ry="13" fill="var(--paper)" stroke="var(--navy)" stroke-width="1"/>
    <text class="spec" x="283" y="358" text-anchor="middle" font-size="6.5">PRODUCT OF</text>
    <text class="spec" x="283" y="367" text-anchor="middle" font-size="6.5">NETHERLANDS</text>
    <text class="spec" x="352" y="365" text-anchor="middle" font-size="10">VOL. 500 ML</text>
  </svg>

  <!-- Option 2 -->
  <svg class="label label--classic-orange" width="570" height="425" viewBox="0 0 570 425">
    <rect width="570" height="425" fill="var(--paper)"/>
    <g class="frame">
      <use href="#corner-bracket" x="24" y="26" width="130" height="100"/>
      <use href="#corner-bracket" width="130" height="100" transform="translate(546 26) scale(-1 1)"/>
      <use href="#corner-bracket" width="130" height="100" transform="translate(24 400) scale(1 -1)"/>
      <use href="#corner-bracket" width="130" height="100" transform="translate(546 400) scale(-1 -1)"/>
    </g>
    <text class="tag" x="136" y="82" text-anchor="middle">100% Natural Botanicals</text>
    <line x1="84" y1="89" x2="188" y2="89" stroke="var(--navy)" stroke-width="1"/>
    <text class="tag" x="437" y="82" text-anchor="middle">No Artificial Flavouring</text>
    <line x1="385" y1="89" x2="489" y2="89" stroke="var(--navy)" stroke-width="1"/>

    <text class="brand" text-anchor="middle"><tspan x="283" y="84" font-size="28" letter-spacing="2">VANTOOR</tspan><tspan x="283" y="114" font-size="13" letter-spacing="4">DISTILLERY</tspan></text>

    <text class="title" x="283" y="192" text-anchor="middle" font-size="66" fill="var(--orange)" textLength="380" lengthAdjust="spacingAndGlyphs">VANTOOR</text>
    <polygon points="156,226 238,224 238,234 166,234" fill="var(--orange)"/>
    <polygon points="328,224 410,226 400,234 328,234" fill="var(--orange)"/>
    <text class="title" x="283" y="240" text-anchor="middle" font-size="52" fill="var(--orange)" textLength="104" lengthAdjust="spacingAndGlyphs">GIN</text>
    <line x1="188" y1="254" x2="378" y2="254" stroke="var(--navy)" stroke-width="1"/>
    <text class="caps-serif" x="283" y="267" text-anchor="middle" font-size="11" letter-spacing="1.5">PREMIUM</text>
    <text class="caps-serif" x="283" y="285" text-anchor="middle" font-size="11" textLength="360" lengthAdjust="spacing">DISTILLED AND BOTTLED BY VANTOOR DISTILLERY</text>
    <text class="caps-sans" x="283" y="316" text-anchor="middle" font-size="27" fill="var(--navy)" textLength="288" lengthAdjust="spacingAndGlyphs">LONDON DRY GIN</text>
    <text class="caps-serif" x="283" y="329" text-anchor="middle" font-size="8" letter-spacing="0.5">HANDCRAFTED IN SMALL BATCH</text>
    <line x1="163" y1="334" x2="403" y2="334" stroke="var(--navy)" stroke-width="1"/>
    <line x1="174" y1="346" x2="408" y2="346" stroke="var(--navy)" stroke-width="1"/>
    <line x1="174" y1="371" x2="408" y2="371" stroke="var(--navy)" stroke-width="1"/>
    <text class="spec" x="212" y="363" text-anchor="middle" font-size="10">50 CL|43% ALC.</text>
    <ellipse cx="281" cy="359" rx="31" ry="13" fill="var(--paper)" stroke="var(--navy)" stroke-width="1"/>
    <text class="spec" x="281" y="356" text-anchor="middle" font-size="6.5">PRODUCT OF</text>
    <text class="spec" x="281" y="365" text-anchor="middle" font-size="6.5">NETHERLANDS</text>
    <text class="spec" x="350" y="363" text-anchor="middle" font-size="10">VOL. 500 ML</text>
  </svg>

  <!-- Option 3 -->
  <svg class="label label--badge" width="560" height="410" viewBox="0 0 560 410">
    <defs>
      <path id="badge-lower-arc" d="M193 115 A82 100 0 0 0 357 115"/>
    </defs>
    <polygon class="badge-body" points="0,212 556,14 556,406 0,406" fill="var(--navy)"/>
    <polyline points="8,219 548,27 548,398 8,398 8,219" fill="none" stroke="var(--white)" stroke-width="1"/>

    <g class="seal">
      <ellipse cx="275" cy="115" rx="94" ry="114" fill="var(--white)"/>
      <ellipse cx="275" cy="115" rx="86" ry="105" fill="none" stroke="var(--navy)" stroke-width="2"/>
      <path class="banner" d="M109 68 H440 A12 12 0 0 0 452 80 V158 A12 12 0 0 0 440 170 H109 A12 12 0 0 0 97 158 V80 A12 12 0 0 0 109 68 Z" fill="var(--white)" stroke="var(--navy)" stroke-width="2"/>
      <rect x="110" y="88" width="330" height="74" fill="none" stroke="var(--navy)" stroke-width="1"/>
      <text class="brand" x="275" y="62" text-anchor="middle" font-size="24" letter-spacing="1.5">VANTOOR</text>
      <line x1="205" y1="79" x2="235" y2="79" stroke="var(--navy)" stroke-width="1"/>
      <line x1="315" y1="79" x2="345" y2="79" stroke="var(--navy)" stroke-width="1"/>
      <text class="caps-sans" x="275" y="83" text-anchor="middle" font-size="10" font-weight="600" fill="var(--navy)" letter-spacing="2.5">DISTILLERY</text>
      <text x="275" y="139" text-anchor="middle" font-family="'Playfair Display', serif" font-weight="700" font-size="46" fill="var(--navy)" textLength="290" lengthAdjust="spacingAndGlyphs">VANTOOR GIN</text>
      <rect x="235" y="147" width="80" height="7" fill="var(--navy)" opacity="0.3" role="img" aria-label="Scroll flourish"/>
      <text class="caps-sans" x="275" y="188" text-anchor="middle" font-size="12" font-weight="700" fill="var(--navy)">PREMIUM</text>
      <text class="caps-sans" font-size="9" font-weight="500" fill="var(--navy)" letter-spacing="0.6">
        <textPath href="#badge-lower-arc" startOffset="50%" text-anchor="middle">HANDCRAFTED IN SMALL BATCH</textPath>
      </text>
    </g>

    <text class="caps-sans" x="275" y="272" text-anchor="middle" font-size="29" font-weight="700" fill="var(--white)" letter-spacing="2">LONDON DRY GIN</text>
    <line x1="8" y1="280" x2="548" y2="280" stroke="var(--white)" stroke-width="1"/>
    <text class="caps-sans" x="275" y="303" text-anchor="middle" font-size="12" font-weight="500" fill="var(--white)">100% NATURAL BOTANICALS ● NO ARTIFICIAL FLAVOURING</text>
    <text class="caps-sans" x="275" y="319" text-anchor="middle" font-size="12" font-weight="500" fill="var(--white)">DISTILLED AND BOTTLED BY VANTOOR DISTILLERY</text>
    <line x1="22" y1="328" x2="536" y2="328" stroke="var(--white)" stroke-width="1"/>
    <text x="30" y="362" font-family="'Tinos', serif" font-size="18" fill="var(--white)" textLength="110" lengthAdjust="spacingAndGlyphs">50 CL|43% ALC.</text>
    <text x="281" y="362" text-anchor="middle" font-family="'Tinos', serif" font-size="18" fill="var(--white)" textLength="228" lengthAdjust="spacingAndGlyphs">PRODUCT OF NETHERLANDS</text>
    <text x="522" y="362" text-anchor="end" font-family="'Tinos', serif" font-size="18" fill="var(--white)" textLength="86" lengthAdjust="spacingAndGlyphs">VOL. 500 ML</text>
  </svg>

  <p class="option-caption option-caption--1">OPTION1</p>
  <p class="option-caption option-caption--2">OPTION2</p>
  <p class="option-caption option-caption--3">OPTION3</p>
</main>
</body>
</html>
```